New Public Cloud Consulting Needs Powerpoint Template

Setting up a new consulting practice and need a powerpoint template and design that reflects our vision. We focus on KRT Public Cloud only. We want to emphasize innovation, cloud, speed. We are based in Asia, with headquarters in Singapore. We serve Asia and Europe customers. The attached file is the current template and logo that we use. However it is not dynamic enough. Blue is the color of our logo - but we must have other colors that complement the blue.

Target Market(s)

Innovation, cloud, advisory

Font styles to use
Other font styles liked:
• We want a different font that what is included in the file.

Requirements
Must have
• Logo which is included in the sample template and blue color - however we want other colors included. To date - most of the designs are completely blue - which we do not want. Additionally we need to create an image of innovation, future vision. Please do not include a picture of a cloud. That is not innovative.
Nice to have
• Would be nice to show people in some of the slides - professional etc. There is one slide in the attached presentation that gives you an idea of this concept. How else can we do this ?

```html
<!DOCTYPE html>
<html lang="en">
<head>
<meta charset="UTF-8">
<title>Everyone Talks about Cloud &amp; Digital Transformation</title>
<link rel="stylesheet" href="https://fonts.googleapis.com/css2?family=Poppins:ital,wght@0,400;0,500;0,700;1,400&display=swap">
<style>
  :root {
    --deep-navy: #1a1f8f;
    --royal-blue: #2a3ad6;
    --violet: #7a3ee8;
    --orchid: #b15cf0;
    --lilac: #c77dff;
    --sky-band: #3b7be6;
    --lime: #8fd14f;
    --white: #ffffff;
    --photo-light: #d9d4cc;
    --photo-mid: #9a8f86;
    --photo-dark: #4a4550;
  }
  * { margin: 0; padding: 0; box-sizing: border-box; }
  html, body {
    width: 1200px;
    height: 675px;
    overflow: hidden;
    background: var(--deep-navy);
  }
  .slide {
    position: relative;
    width: 1200px;
    height: 675px;
    overflow: hidden;
    font-family: "Poppins", sans-serif;
    color: var(--white);
    background:
      radial-gradient(ellipse 520px 300px at 160px 560px, rgba(177, 92, 240, 0.55), transparent 70%),
      radial-gradient(ellipse 600px 420px at 520px 420px, rgba(122, 62, 232, 0.55), transparent 70%),
      linear-gradient(160deg, #1d2ab8 0%, var(--royal-blue) 35%, #3a2fcf 60%, var(--violet) 100%);
  }
  .hero-visual {
    position: absolute;
    inset: 0;
    width: 1200px;
    height: 675px;
  }
  .headline {
    position: absolute;
    left: 58px;
    top: 66px;
    font-weight: 700;
    font-size: 46px;
    line-height: 64px;
    letter-spacing: -0.2px;
  }
  .tagline {
    position: absolute;
    left: 58px;
    top: 278px;
    font-weight: 400;
    font-style: italic;
    font-size: 32px;
    color: var(--lime);
  }
  .brand {
    position: absolute;
    left: 60px;
    top: 508px;
    display: flex;
    align-items: center;
    gap: 16px;
  }
  .brand-mark {
    width: 22px;
    height: 22px;
    border-radius: 50%;
    background: var(--white);
  }
  .brand-name {
    font-weight: 500;
    font-size: 40px;
    line-height: 44px;
    color: var(--white);
  }
  .brand-name small {
    display: block;
    font-size: 22px;
    line-height: 26px;
    font-weight: 500;
  }
</style>
</head>
<body>
  <main class="slide">
    <svg class="hero-visual" viewBox="0 0 1200 675" aria-hidden="false">
      <defs>
        <linearGradient id="photo-tones" x1="0" y1="0" x2="1" y2="1">
          <stop offset="0" stop-color="var(--photo-light)"/>
          <stop offset="0.5" stop-color="var(--photo-mid)"/>
          <stop offset="1" stop-color="var(--photo-dark)"/>
        </linearGradient>
        <linearGradient id="band-blue" x1="0" y1="0" x2="1" y2="1">
          <stop offset="0" stop-color="#4f8cf0"/>
          <stop offset="1" stop-color="#2e5fd8"/>
        </linearGradient>
        <linearGradient id="band-violet" x1="0" y1="0" x2="1" y2="1">
          <stop offset="0" stop-color="#a55cf2" stop-opacity="0.85"/>
          <stop offset="1" stop-color="#7a3ee8" stop-opacity="0.7"/>
        </linearGradient>
      </defs>

      <polygon class="photo-area" role="img"
        aria-label="Photo of a smiling team of young professionals gathered around a tablet in a bright modern office"
        points="830,0 1200,0 1200,675 830,675 636,338"
        fill="url(#photo-tones)"/>

      <polygon class="accent-band" points="840,0 880,0 660,300 620,300" fill="url(#band-blue)" opacity="0.95"/>
      <polygon class="accent-band" points="885,0 930,0 745,240 700,240" fill="url(#band-blue)" opacity="0.6"/>
      <polygon class="accent-band" points="600,290 660,290 620,338 585,338" fill="var(--violet)" opacity="0.8"/>

      <polygon class="accent-tint" points="900,340 1200,110 1200,675 1060,675" fill="var(--lilac)" opacity="0.35"/>
      <polygon class="accent-tint" points="1080,250 1200,150 1200,420" fill="var(--orchid)" opacity="0.4"/>
      <polygon class="accent-tint" points="520,675 770,420 870,675" fill="url(#band-violet)"/>
      <polygon class="accent-tint" points="700,675 860,500 990,675" fill="var(--orchid)" opacity="0.55"/>
      <polygon class="accent-tint" points="1040,480 1200,330 1200,675 1150,675" fill="var(--violet)" opacity="0.45"/>
    </svg>

    <h1 class="headline">Everyone Talks about<br>Cloud &amp; Digital<br>Transformation</h1>
    <p class="tagline">We do it differently</p>

    <div class="brand">
      <span class="brand-mark"></span>
      <span class="brand-name">Orbit<small>Consulting Group</small></span>
    </div>
  </main>
</body>
</html>
```